Redesign current website

Current website www.kelvatreproperty.com.au needs to be redone.

Content will be the same however the visual look needs to be upgraded.

Need ability to WYSIWYG editor any of the pages, including embedding videos and images throughout the pages.

It currently looks dated and a bit dodgy. Need the same functionality (i.e. submission forms etc...) however need it to look much more modern.

Needs to be easy to navigate, and look fresh, credible and professional.

Must be mobile compatible and SEO friendly.

Not interested in sites that look like the 1000+ one websites templates.

```html
<!DOCTYPE html>
<html lang="en">
<head>
<meta charset="utf-8">
<title>Kelvatre Property</title>
<link href="https://fonts.googleapis.com/css2?family=Oswald:wght@400;500&family=Open+Sans:wght@400;600&display=swap" rel="stylesheet">
<style>
:root{
  --royal:#0c3fc4;
  --navy:#0b3a8e;
  --yellow:#f5d80a;
  --amber:#f7b800;
  --ink:#222;
  --grey-text:#7a7a7a;
  --light:#ebebeb;
  --cyan:#1ec6e6;
  --black:#0d0d0d;
  --white:#fff;
}
*{margin:0;padding:0;box-sizing:border-box}
html,body{width:720px;height:1200px;overflow:hidden;background:var(--white)}
body{position:relative;font-family:"Open Sans",Arial,sans-serif;color:var(--ink)}
.abs{position:absolute}

.topbar{left:0;top:0;width:720px;height:66px;background:var(--royal)}
.brand{left:36px;top:12px;font-family:"Oswald",sans-serif;font-weight:500;font-size:28px;line-height:40px;color:var(--yellow);display:flex;align-items:center;gap:8px;white-space:nowrap}
.brand .dot{width:22px;height:22px;border-radius:50%;background:var(--yellow)}
.contact{right:28px;top:19px;text-align:right;color:var(--white);font-size:10px;line-height:14px;white-space:nowrap}
.contact svg{vertical-align:middle;margin-left:4px}

.nav{left:0;top:66px;width:720px;height:32px;background:linear-gradient(var(--yellow),var(--amber));display:flex;align-items:stretch}
.nav a{font-size:9px;color:#3a2a00;text-decoration:none;display:flex;align-items:center;justify-content:center;border-right:1px solid rgba(0,0,0,.1);white-space:nowrap}
.nav .home{margin-left:33px;width:60px;background:var(--royal);color:var(--yellow)}
.nav .alert{position:absolute;left:570px;top:0;height:32px;width:122px;background:var(--amber);color:var(--white);font-weight:600;font-size:10.5px;border:none}

.hero{left:0;top:98px;width:720px;height:330px;background:var(--navy)}
.hero-art{left:40px;top:98px;width:240px;height:330px;background:linear-gradient(180deg,#dfe6f2,#b9c6dd)}
.hero-ghost{left:464px;top:98px;width:240px;height:330px;background:linear-gradient(180deg,rgba(255,255,255,.08),rgba(255,255,255,.03))}
.hero-name{left:338px;top:222px;font-family:"Oswald",sans-serif;font-weight:500;font-size:28px;line-height:40px;color:var(--yellow);display:flex;align-items:center;gap:8px;white-space:nowrap}
.hero-name .dot{width:24px;height:24px;border-radius:50%;background:var(--yellow)}
.hero-text{left:338px;top:266px;width:292px;color:var(--white);font-size:9.4px;line-height:11px}
.btn-yellow{left:338px;top:307px;width:76px;height:22px;background:var(--yellow);color:var(--ink);font-size:7px;font-weight:600;display:flex;align-items:center;justify-content:center}
.dots{left:592px;top:394px;display:flex;gap:6px}
.dots i{width:8px;height:8px;border-radius:50%;background:var(--white)}
.dots i.on{background:transparent;border:1.5px solid var(--yellow)}

.welcome-title{left:33px;top:456px;font-family:"Oswald",sans-serif;font-weight:400;font-size:22px;line-height:30px;color:var(--ink);white-space:nowrap}
.welcome-text{left:34px;top:492px;width:440px;font-size:8.6px;line-height:13.5px;color:var(--grey-text)}
.btn-blue{left:33px;top:616px;width:69px;height:21px;background:var(--royal);color:var(--yellow);font-size:7.5px;display:flex;align-items:center;justify-content:center}
.video{left:492px;top:461px;width:200px;height:177px;background:linear-gradient(180deg,#1a1a1a,#3a3a3a)}
.video .bar{position:absolute;left:0;bottom:0;width:100%;height:15px;background:#111}
.video .play{position:absolute;left:84px;top:66px}

.features{left:0;top:659px;width:720px;height:117px;background:linear-gradient(var(--yellow),var(--amber))}
.feature{position:absolute;top:0;width:210px;height:117px}
.feature h3{position:absolute;left:0;top:22px;font-weight:400;font-size:10px;line-height:14px;color:var(--ink);white-space:nowrap}
.feature p{position:absolute;left:0;top:43px;width:206px;font-size:7.4px;line-height:10px;color:#2a2000}
.feature .more{position:absolute;left:0;top:85px;height:19px;padding:0 9px;font-size:7.5px;display:flex;align-items:center;background:var(--yellow);color:var(--ink);border-radius:2px;white-space:nowrap}
.feature .more.dark{left:-2px;background:#1b1a10;color:var(--yellow)}
.divider{position:absolute;top:0;width:1px;height:117px;background:rgba(255,255,255,.45)}

.newsletter{left:0;top:776px;width:720px;height:182px;background:var(--light)}
.newsletter h2{position:absolute;left:0;width:720px;top:28px;text-align:center;font-family:"Oswald",sans-serif;font-weight:400;font-size:23px}
.email{left:167px;top:850px;width:270px;height:39px;background:var(--white);border:1px solid #ddd;font-size:11px;color:#666;display:flex;align-items:center;padding-left:12px}
.subscribe{left:445px;top:850px;width:125px;height:39px;background:linear-gradient(var(--yellow),var(--amber));color:var(--white);font-size:17px;display:flex;align-items:center;justify-content:center}
.news-text{left:170px;top:905px;width:380px;text-align:center;font-size:10.5px;line-height:13.5px;color:#555}

.feed{left:0;top:958px;width:720px;height:169px;background:var(--cyan)}
.feed h2{position:absolute;left:0;width:720px;top:24px;text-align:center;font-family:"Oswald",sans-serif;font-weight:400;font-size:22px;color:var(--white)}
.avatar{left:153px;top:1030px;width:54px;height:54px;border-radius:50%;border:3px solid var(--white);background:linear-gradient(#c9b59a,#6f6a66)}
.feed-text{left:230px;top:1034px;width:355px;font-size:8.7px;line-height:10.8px;color:var(--white)}
.feed-text b{display:block;font-size:10.5px;margin-top:2px}
.arrow{top:1047px}

.footer{left:0;top:1127px;width:720px;height:73px;background:var(--black)}
.foot-brand{left:38px;top:1153px;font-family:"Oswald",sans-serif;font-weight:500;font-size:15px;color:var(--yellow);white-space:nowrap}
.foot-links{left:0;top:1152px;width:720px;text-align:center;font-size:8px;color:var(--white)}
.copy{left:0;top:1170px;width:720px;text-align:center;font-size:7px;color:#888}
.social{left:614px;top:1153px;display:flex;gap:6px}
.social i{width:22px;height:22px;border-radius:50%;border:1.5px solid #ccc}
</style>
</head>
<body>

<header class="abs topbar"></header>
<div class="abs brand"><span class="dot"></span>Kelvatre Property</div>
<div class="abs contact">
  Call us today &nbsp;- 1800 555 014
  <svg width="10" height="8" viewBox="0 0 10 8"><path d="M1 3c2-2.5 6-2.5 8 0v1.2H7V3H3v1.2H1z M2 5h6l1 3H1z" fill="#f5d80a"/></svg><br>
  info@kelvatreproperty.com.au
  <svg width="10" height="8" viewBox="0 0 10 8"><rect x="0.5" y="0.5" width="9" height="7" fill="#f5d80a"/><path d="M0.5 0.5l4.5 4 4.5-4" stroke="#0c3fc4" fill="none"/></svg>
</div>

<nav class="abs nav">
  <a class="home">Home</a>
  <a style="width:106px">Our Solutions</a>
  <a style="width:105px">How It Works</a>
  <a style="width:85px">About Us</a>
  <a style="width:90px">Contact Us</a>
  <a class="alert">Private Render Alert</a>
</nav>

<section class="abs hero"></section>
<div class="abs hero-art" role="img" aria-label="Illustration of a hand passing a house key to an open hand"></div>
<div class="abs hero-ghost" role="img" aria-label="Faint background illustration of hands and a house key"></div>
<div class="abs hero-name"><span class="dot"></span>Kelvatre Property</div>
<p class="abs hero-text">Lorem ipsum dolor sit amet, consectetur adipiscing elit, sed do eiusmod tempor incididunt ut labore et dolore magna aliqua. Ut enim ad minim veniamexercitation ullamco laboris nisi.</p>
<div class="abs btn-yellow">KNOW MORE</div>
<div class="abs dots"><i></i><i></i><i></i><i class="on"></i><i></i></div>

<h1 class="abs welcome-title">Welcome to Kelvatre Property</h1>
<p class="abs welcome-text">Lorem ipsum dolor sit amet, consectetur adipiscing elit, sed do eiusmod tempor incididunt ut labore et dolore magna aliqua. Ut enim ad minim veniam, quis nostrud exercitation ullamco laboris nisi ut aliquip ex ea commodo consequat. Duis aute irure dolor in reprehenderit in voluptate velit esse cillum dolore eu fugiat nulla pariatur. Excepteur sint occaecat cupidatat non proident, officia deserunt mollit anim id est laborum.Lorem ipsum dolor sit amet, consectetur adipiscing elit, sed do eiusmod tempor incididunt ut labore et dolore magna aliqua. Ut enim ad minim veniam, quis nostrud exercitation ullamco laboris nisi ut aliquip ex ea commodo consequat. Duis aute irure dolor in reprehenderit in voluptate velit esse cillum dolore eu fugiat nulla pariatur. Excepteur sint occaecat cupidatat non proident, officia deserunt mollit anim id est laborum.</p>
<div class="abs btn-blue">READ MORE</div>
<div class="abs video" role="img" aria-label="Welcome video of the company founder speaking to camera">
  <svg class="play" width="34" height="34" viewBox="0 0 34 34"><circle cx="17" cy="17" r="16" fill="rgba(0,0,0,.5)" stroke="#ddd" stroke-width="1.5"/><path d="M13 10l11 7-11 7z" fill="#eee"/></svg>
  <div class="bar"></div>
</div>

<section class="abs features">
  <div class="feature" style="left:32px">
    <h3>FAST MONEY</h3>
    <p>We've bought property in as little as seven (7) days. If you call us early enough, we can save you from bankruptcy, foreclosure or repossession.</p>
    <span class="more dark">Read More</span>
  </div>
  <div class="divider" style="left:241px"></div>
  <div class="feature" style="left:261px">
    <h3>MAXIMUM PROFIT</h3>
    <p>We need to be able to sit on either side of the negotiation table and feel like we've negotiated a fair deal for all parties.</p>
    <span class="more">Read More</span>
  </div>
  <div class="divider" style="left:481px"></div>
  <div class="feature" style="left:504px">
    <h3>BENEFITS</h3>
    <p>- No Advertising Fees<br>- No Agent Fees<br>- No Dodgey Real Estate Agents</p>
    <span class="more">Read More</span>
  </div>
</section>

<section class="abs newsletter"><h2>Subscribe to our newsletter</h2></section>
<div class="abs email">Email Address</div>
<div class="abs subscribe">Subscibe</div>
<p class="abs news-text">Lorem ipsum dolor sit amet, consectetur adipiscing elit, sed do eiusmod tempor incididunt labore et dolore magna aliqua.</p>

<section class="abs feed"><h2>Social Feed</h2></section>
<svg class="abs arrow" style="left:80px" width="12" height="20" viewBox="0 0 12 20"><path d="M10 2L2 10l8 8" stroke="#fff" stroke-width="1.6" fill="none"/></svg>
<div class="abs avatar" role="img" aria-label="Profile photo of the post author"></div>
<p class="abs feed-text">Lorem ipsum dolor sitera amet, consectetur &nbsp;elit, do loren are doLorem ipsum dolor sitera amet, consectetur &nbsp;elit, do loren are doLorem ipsum dolor sitera amet, consectetur &nbsp;elit, do loren are doLorem ipsum dolor sitera amet,...<b>- Dolore magna aliqua</b></p>
<svg class="abs arrow" style="left:613px" width="12" height="20" viewBox="0 0 12 20"><path d="M2 2l8 8-8 8" stroke="#fff" stroke-width="1.6" fill="none"/></svg>

<footer class="abs footer"></footer>
<div class="abs foot-brand">Kelvatre Property</div>
<div class="abs foot-links">Home &nbsp;| &nbsp;Our Solutions &nbsp;| &nbsp;How It Works &nbsp;| &nbsp;About Us &nbsp;| &nbsp;Contact Us</div>
<div class="abs copy">Copyright @ Kelvatre Property &nbsp;- 2015</div>
<div class="abs social"><i></i><i></i><i></i></div>

</body>
</html>
```